Brightfernrx website

We are a weight loss clinic and we need a website built. please look at these websites for content and style. Just need like 5 pages see samples. AI files of logo are not avail yet so use sample for place set

https://glowshiftstudio.com/
ortanvital.com
https://pinecrestclinicalbodybalance.com/
https://yourslimmingnook.com/
https://qrvskinstudio.com/treatments/weight-loss-injections/

Target Market(s)

Women

Industry/Entity Type

weight loss

Coding

Coded - Design and coding required

Number of Pages Required

5+ page

Requirements
Nice to have
• please make look like a medspa website

```html
<!DOCTYPE html>
<html lang="en">
<head>
<meta charset="utf-8">
<title>Brightfernrx — Weight Loss Clinic</title>
<link rel="stylesheet" href="https://fonts.googleapis.com/css2?family=Montserrat:wght@400;500;600;700;800&display=swap">
<style>
:root{
  --teal:#1f8c7a;
  --teal-dark:#136a5f;
  --orange:#f0845a;
  --cream:#fdf8f6;
  --white:#ffffff;
  --ink:#1c1c1c;
  --field:#e2e2e2;
}
*{box-sizing:border-box;margin:0;padding:0}
html,body{width:1200px;height:3892px;overflow:hidden;background:var(--white)}
body{font-family:"Montserrat",sans-serif;color:var(--ink)}
.page{position:relative;width:1200px;height:3892px;overflow:hidden}
.abs{position:absolute}
.wave{position:absolute;left:0;width:1200px;display:block}

/* header */
.brand{left:209px;top:26px;font-size:30px;font-weight:700;letter-spacing:1px;color:var(--white)}
.nav{left:524px;top:34px;display:flex;gap:17px;align-items:center;font-size:11.5px;color:var(--white)}
.nav .book{background:var(--orange);padding:3px 6px;border:1px solid #fff3}

/* text column blocks (flow layout, no overlaps) */
.col{position:absolute;display:flex;flex-direction:column;align-items:flex-start}
.kicker{font-size:16px;font-weight:600;letter-spacing:.3px;color:var(--ink)}
.kicker.light{color:var(--white)}
.heading{font-size:24px;font-weight:800;line-height:29px;color:var(--orange);text-transform:uppercase;letter-spacing:.3px;margin-top:12px}
.body{font-size:12px;line-height:15px;color:#333;margin-top:10px}
.body.light{color:#e9f5f2}
.lead{font-size:14px;font-weight:700;color:var(--ink);margin-top:16px}
.lead.light{color:var(--white)}
.lead + .body{margin-top:14px}
.body + .body{margin-top:16px}
.btn{display:inline-block;background:var(--orange);color:var(--ink);font-size:11px;font-weight:500;padding:5px 6px;border:1px solid #0002;margin-top:22px}

/* hero */
.hero{left:209px;top:196px;width:350px}
.hero-title{font-size:34px;font-weight:800;line-height:41px;color:var(--orange)}
.hero-text{margin-top:12px;font-size:13.5px;line-height:17px;color:var(--white)}
.hero-lead{margin-top:23px;font-size:14px;font-weight:700;color:var(--white)}
.hero .btn{margin-top:27px}
.hero-photo{left:560px;top:84px;width:380px;height:500px;border-radius:190px 190px 0 0;background:linear-gradient(180deg,#c99a7c 0%,#6d4c3c 45%,#1d1d1d 100%);opacity:.9}

/* cards */
.card{top:665px;width:245px;height:208px;border-radius:4px;text-align:center;padding-top:22px;color:var(--white)}
.card.teal{background:linear-gradient(180deg,var(--teal),var(--teal-dark))}
.card.orange{background:var(--orange)}
.card h3{font-size:16px;font-weight:500;line-height:19px;margin-top:12px;color:var(--orange)}
.card.orange h3{color:var(--white)}
.card p{font-size:10px;line-height:12px;margin:6px 22px 0}

/* testimonial */
.quote-block{left:594px;top:2780px;width:400px}
.quote{font-size:16px;line-height:20px;color:var(--white)}
.quote-name{margin-top:8px;font-size:17px;font-weight:700;color:var(--orange)}

.photo{position:absolute}
</style>
</head>
<body>
<div class="page">

  <!-- hero band -->
  <svg class="wave" style="top:0" width="1200" height="590" viewBox="0 0 1200 590" aria-hidden="true">
    <defs><linearGradient id="heroGrad" x1="0" y1="0" x2="0" y2="1"><stop offset="0" stop-color="#1f8c7a"/><stop offset="1" stop-color="#12695e"/></linearGradient></defs>
    <path d="M0 0H1200V578C1000 600 800 570 600 565C400 560 200 565 0 560Z" fill="url(#heroGrad)"/>
    <path d="M0 60C120 20 220 110 330 60C420 20 380 0 300 0H0Z" fill="#ffffff" opacity=".05"/>
  </svg>
  <div class="abs brand">Brightfernrx</div>
  <nav class="abs nav"><span>Home</span><span>About Us</span><span>What We Do</span><span>Resource</span><span>Contact US</span><span class="book">Book Appointment</span></nav>
  <div class="col hero">
    <h1 class="hero-title">LOSS WEIGHT<br>&amp; FEEL GREAT</h1>
    <p class="hero-text">Lorem ipsum dolor sit amet, consectetur adipiscing elit, sed do eiusmod tempor incididunt ut labore et dolore magna aliqua. Quis ipsum sus-</p>
    <div class="hero-lead">Nullam eros sem, gravida tincidunt diam</div>
    <a class="btn">READ MORE</a>
  </div>
  <div class="abs hero-photo" role="img" aria-label="Smiling woman in sportswear measuring her waist with a tape"></div>

  <!-- feature cards -->
  <div class="abs card teal" style="left:209px">
    <svg width="58" height="58" viewBox="0 0 58 58" fill="none" stroke="#fff" stroke-width="2.5" aria-hidden="true"><rect x="6" y="14" width="46" height="38" rx="8"/><path d="M21 14V8h16v6"/><path d="M25 25h8v6h6v8h-6v6h-8v-6h-6v-8h6z"/></svg>
    <h3>Weight Can be a<br>Serious Matter</h3>
    <p>Lorem ipsum dolor sit amet, consectetur adipiscing elit. In tristique mauris eget commodo aliquam. Aliquam nec imperdiet sem.</p>
  </div>
  <div class="abs card orange" style="left:477px">
    <svg width="58" height="58" viewBox="0 0 58 58" fill="none" stroke="#fff" stroke-width="2.5" aria-hidden="true"><rect x="6" y="6" width="46" height="46" rx="10"/><circle cx="29" cy="22" r="9"/><path d="M29 22l3-4"/></svg>
    <h3>Lose Weight, Only<br>to Regain it Later?</h3>
    <p>Lorem ipsum dolor sit amet, consectetur adipiscing elit. In tristique mauris eget commodo aliquam. Aliquam nec imperdiet sem.</p>
  </div>
  <div class="abs card teal" style="left:745px">
    <svg width="58" height="58" viewBox="0 0 58 58" fill="none" stroke="#fff" stroke-width="2.5" aria-hidden="true"><rect x="5" y="18" width="36" height="18" rx="9" transform="rotate(-40 23 27)"/><path d="M18 20l11 13"/><circle cx="41" cy="41" r="10"/><path d="M34 48l14-14"/></svg>
    <h3>Obesity is Rarely a<br>Simple Problem</h3>
    <p>Lorem ipsum dolor sit amet, consectetur adipiscing elit. In tristique mauris eget commodo aliquam. Aliquam nec imperdiet sem.</p>
  </div>

  <!-- tools section -->
  <div class="col" style="left:209px;top:958px;width:375px">
    <div class="kicker">LOREM IPSUM</div>
    <h2 class="heading">Providing the tools you<br>need to achieve success</h2>
    <p class="body">Etiam rutrum semper orci, quis dignissim quam varius sit amet. Cras blandit egestas massa id sollicitudin. Integer faucibus quis urna id sodales. Proin nisl massa, sollicitudin sit amet placerat eget, accumsan non elit. Nam vel mauris a libero facilisis euismod nec sed orci. Nam vulputate in odio non bibendum.</p>
    <div class="lead">Nulla auctor diam id iaculis tristique.</div>
    <p class="body">Lorem ipsum dolor sit amet, consectetur adipiscing elit. Fusce elit leo, tincidunt blandit libero quis, mattis egestas urna. Integer elementum eros ut justo commodo hendrerit.</p>
    <p class="body">Ut diam est, fringilla sit amet leo et, suscipit feugiat ante.</p>
    <a class="btn">READ MORE</a>
  </div>
  <svg class="photo" style="left:640px;top:945px" width="400" height="390" viewBox="0 0 400 390" role="img" aria-label="Two women smiling while training in a gym">
    <defs><linearGradient id="gymGrad" x1="0" y1="0" x2="1" y2="1"><stop offset="0" stop-color="#4a4a4a"/><stop offset=".5" stop-color="#b89a78"/><stop offset="1" stop-color="#2a2a2a"/></linearGradient></defs>
    <circle cx="203" cy="191" r="189" fill="#1d7d6d"/>
    <circle cx="203" cy="191" r="172" fill="url(#gymGrad)"/>
    <circle cx="67" cy="309" r="71" fill="#17665b" opacity=".9"/>
  </svg>

  <!-- evidence band -->
  <svg class="wave" style="top:1400px" width="1200" height="565" viewBox="0 0 1200 565" aria-hidden="true">
    <defs><linearGradient id="bandGrad" x1="0" y1="0" x2="0" y2="1"><stop offset="0" stop-color="#238b7a"/><stop offset="1" stop-color="#136a5f"/></linearGradient></defs>
    <path d="M0 30C300 10 600 -5 1200 8V545C1000 560 800 520 600 535C400 550 200 560 0 528Z" fill="url(#bandGrad)"/>
  </svg>
  <svg class="photo" style="left:100px;top:1478px" width="430" height="420" viewBox="0 0 430 420" role="img" aria-label="Woman in pink sportswear holding greens beside an exercise ball">
    <defs><linearGradient id="yogaGrad" x1="0" y1="0" x2="1" y2="1"><stop offset="0" stop-color="#f6b81e"/><stop offset=".6" stop-color="#f4a82a"/><stop offset="1" stop-color="#c9c9c9"/></linearGradient></defs>
    <path d="M170 6C270 2 420 120 420 260C420 380 330 418 230 418C110 418 10 350 6 230C2 130 70 10 170 6Z" fill="#f0845a"/>
    <path d="M170 14C265 10 410 125 410 258C410 370 325 408 230 408C115 408 18 345 14 230C10 135 75 18 170 14Z" fill="url(#yogaGrad)"/>
    <path d="M300 24C350 14 410 50 400 110C392 160 330 160 300 130C270 100 260 34 300 24Z" fill="#f0845a" opacity=".8"/>
  </svg>
  <div class="col" style="left:594px;top:1494px;width:385px">
    <div class="kicker light">LOREM IPSUM</div>
    <h2 class="heading">Evidence based<br>medications &amp; treatments</h2>
    <p class="body light">Duis elit nisi, auctor id placerat dignissim, suscipit id ante. Duis lobortis tincidunt ante eget rutrum. Sed purus massa, convallis id quam a, lacinia rhoncus est. Vestibulum quis felis nec velit faucibus consectetur. Proin sodales odio ut sapien ultrices, in vehicula metus varius. Praesent fringilla lectus ut odio gravida ultricies.</p>
    <div class="lead light">Integer efficitur felis vel vulputate rhoncus.</div>
    <p class="body light">Ut a purus ut tellus bibendum porttitor ut eu elit. Etiam non commodo nisi, ac malesuada risus. Vestibulum tincidunt massa eu dictum accumsan. Cras sit amet tellus risus.</p>
    <a class="btn">READ MORE</a>
  </div>

  <!-- journey section -->
  <div class="abs" style="left:0;top:1960px;width:1200px;height:690px;background:var(--cream)"></div>
  <div class="col" style="left:209px;top:2126px;width:375px">
    <div class="kicker">LOREM IPSUM</div>
    <h2 class="heading">Start your journey</h2>
    <p class="body">Pellentesque non ipsum ut ipsum euismod commodo. Vivamus dui lacus, fringilla a dictum sed, mattis sit amet mauris. Curabitur accumsan sodales purus, ac iaculis massa suscipit id. Fusce eu orci vel ante tristique mattis. Duis pharetra vehicula ullamcorper. Vivamus mollis egestas nibh ac convallis.</p>
    <div class="lead">Duis accumsan semper sem, non aliquet just.</div>
    <p class="body">Nam in maximus odio. Vestibulum quis pellentesque massa. Aliquam eu pretium nibh, at posuere mi. In mi velit, fringilla ut ligula id, pulvinar imperdiet mauris. Sed efficitur porta rutrum. Etiam eget tellus at orci interdum sagittis at in sem. Curabitur lobortis ullamcorper augue non scelerisque.</p>
    <a class="btn" style="padding:6px 9px">BOOK CONSULTATION</a>
  </div>
  <svg class="photo" style="left:645px;top:2040px" width="555" height="560" viewBox="0 0 555 560" role="img" aria-label="Measuring tape, dumbbell, bathroom scale and fresh vegetables">
    <defs><linearGradient id="scaleGrad" x1="0" y1="0" x2="1" y2="1"><stop offset="0" stop-color="#9a9a96"/><stop offset=".5" stop-color="#c8c6c0"/><stop offset="1" stop-color="#e9e6df"/></linearGradient></defs>
    <path d="M210 2C260 -4 290 14 250 30C210 46 150 48 130 36C110 24 170 8 210 2Z" fill="#1c7c6d"/>
    <path d="M555 20V560C470 520 420 505 300 505C150 505 8 470 4 330C0 200 80 120 200 110C330 100 420 40 555 20Z" fill="#176b60"/>
    <path d="M555 36V540C470 500 420 490 300 490C160 490 20 455 18 330C16 210 90 135 205 126C330 116 420 58 555 36Z" fill="url(#scaleGrad)"/>
  </svg>

  <!-- testimonial band -->
  <svg class="wave" style="top:2630px" width="1200" height="545" viewBox="0 0 1200 545" aria-hidden="true">
    <path d="M0 22C200 6 400 2 600 6C800 10 1000 4 1200 12V505C1000 540 800 480 600 500C400 520 200 535 0 528Z" fill="url(#bandGrad)"/>
  </svg>
  <svg class="photo" style="left:118px;top:2708px" width="430" height="395" viewBox="0 0 430 395" role="img" aria-label="Portrait of a fit woman with crossed arms in a grey sports top">
    <path d="M170 4C280 0 420 70 424 190C428 300 360 386 180 390C60 392 8 340 6 240C4 120 60 8 170 4Z" fill="#f0845a"/>
    <path d="M170 10C275 6 408 76 412 190C416 296 352 376 180 380C66 382 10 330 10 240C10 125 65 14 170 10Z" fill="#3b3d40"/>
    <path d="M330 320C360 300 380 310 370 335C360 360 300 382 280 372C265 364 300 340 330 320Z" fill="#f0845a"/>
  </svg>
  <figure class="col quote-block">
    <blockquote class="quote">“Pellentesque habitant morbi tristique senectus et netus et malesuada fames ac turpis egestas. Nam volutpat at sem in lobortis. Mauris a orci ullamcorper, pellentesque lectus eu, fringilla ante. Cras in sapien aliquam, placerat sem non, luctus lorem. Aliquam lobortis vulputate ex, commodo efficitur dui semper interdum. Vestibulum ante ipsum primis in faucibus orci luctus et ultrices posuere cubilia curae; Phasellus nec libero at orci sagittis sollicitudin in sed augue. Etiam eget tortor ultrices, tempor nunc vitae, dapibus ex.”</blockquote>
    <figcaption class="quote-name">MARLA VESTIN</figcaption>
  </figure>

  <!-- contact form -->
  <div class="col" style="left:209px;top:3316px;width:340px">
    <div class="kicker">LOREM IPSUM</div>
    <h2 class="heading">We want this to be<br>the last weight loss<br>program you do.</h2>
  </div>
  <form class="abs" style="left:639px;top:3271px;width:349px;height:210px;font-size:9px;color:#333">
    <div class="abs" style="left:0;top:0;width:349px;height:24px;background:var(--field);padding:7px 6px">Full Name</div>
    <div class="abs" style="left:0;top:32px;width:169px;height:24px;background:var(--field);padding:7px 6px">Phone</div>
    <div class="abs" style="left:180px;top:32px;width:169px;height:24px;background:var(--field);padding:7px 6px">Email</div>
    <div class="abs" style="left:0;top:65px;width:349px;height:23px;background:var(--field);padding:7px 6px">Weight Loss Treatment</div>
    <div class="abs" style="left:0;top:97px;width:349px;height:56px;background:var(--field);padding:6px 6px">Message (Max. 500 Characters)</div>
    <div class="abs" style="left:6px;top:163px">0 of 500 max characters</div>
    <div class="abs" style="left:0;top:180px;width:159px;height:26px;background:var(--teal-dark);color:var(--white);text-align:center;padding-top:8px">SUBMIT REQUEST</div>
  </form>

  <!-- footer -->
  <svg class="wave" style="top:3580px" width="1200" height="312" viewBox="0 0 1200 312" aria-hidden="true">
    <path d="M0 28C300 0 500 12 700 14C900 16 1050 8 1200 20V312H0Z" fill="url(#bandGrad)"/>
  </svg>
  <footer class="abs" style="left:0;top:3580px;width:1200px;height:312px;color:var(--white);font-size:12.5px">
    <div class="abs" style="left:209px;top:73px;font-weight:700">Menu</div>
    <div class="abs" style="left:209px;top:116px;line-height:27px">Home<br>Services<br>Departments<br>Guide<br>Contact Us</div>
    <div class="abs" style="left:417px;top:73px;font-weight:700">Information</div>
    <div class="abs" style="left:417px;top:116px;line-height:27px">Destination<br>support<br>Term &amp; Condition<br>Privacy</div>
    <div class="abs" style="left:663px;top:73px;font-weight:700">Contact Info</div>
    <div class="abs" style="left:663px;top:116px;line-height:27px">+1 555 0142 7788<br>hello@brightfernrx.com<br>A-1, liquam, ultrices.</div>
    <div class="abs" style="left:923px;top:73px;font-weight:700">Follow on</div>
    <div class="abs" style="left:923px;top:104px;display:flex;gap:5px">
      <span style="width:17px;height:17px;border-radius:50%;background:var(--white)"></span>
      <span style="width:17px;height:17px;border-radius:50%;background:var(--white)"></span>
      <span style="width:17px;height:17px;border-radius:50%;background:var(--white)"></span>
    </div>
    <div class="abs" style="left:177px;top:259px;width:844px;height:3px;background:var(--white)"></div>
    <div class="abs" style="left:209px;top:282px">Copyright © 2021 Lorem Ipsum All Rights Reserved.</div>
    <div class="abs" style="left:775px;top:282px">Terms &amp; Conditions | Privacy Policy</div>
  </footer>

</div>
</body>
</html>
```